Web Design Project

We need to have you design a 7 page design for ecommerce site.

The design will consist of a Home Page, Category Landing Page, Category Product Page, Product Page, Cart Page, Gift Registry Page, and Virtual Place Setting Page

The goal will be a design which is similar to:

http://www.velmora.example/ in terms of layout of the home page

http://www.velmora.example/decor The category landing pages will look a bit like this

http://www.velmora.example/decor/decorative-pillows. The category product pages will look like this , however, will have more of a layered navigation on the left where you can sort by brand, price, finish, etc. instead of ability to shop by category here

http://www.velmora.example/p/corvela-dinnerware The product page can be similar to this one

Please add a product to cart as the cart page can be very similar to the look and feel here.

For the gift registry landing page, here are some examples: http://www.linenhearthplus.example/regHome.asp

http://www.tarrow-brisco.example/registry/

Last, we need to create a virtual place setting app like this: http://www.fornovida.example/style-your-table

But more better and stylish, mapping in with the theme.

Requirements
Must have
• - This needs to have a sophisticated, luxurious look and feel. Please make sure to design a 'showcase' style page for the main categorly landing pages.

```html
<!DOCTYPE html>
<html lang="en">
<head>
<meta charset="utf-8">
<title>Orlin House — Home</title>
<link rel="stylesheet" href="https://fonts.googleapis.com/css2?family=Arimo:wght@400;700&family=Oswald:wght@500;600&family=Great+Vibes&family=Bowlby+One+SC&family=Michroma&family=Play:wght@400&display=swap">
<style>
:root{
  --sage:#8db06a;
  --sage-line:#c9dcb4;
  --ink:#111111;
  --white:#ffffff;
  --charcoal:#333333;
  --violet:#8a0fd6;
  --violet-btn:#9b2ee6;
  --crimson:#b3121a;
  --tile-top:#e8585c;
  --tile-bottom:#b71e24;
}
*{box-sizing:border-box;margin:0;padding:0}
html,body{width:1200px;height:1110px;overflow:hidden;background:var(--white)}
body{position:relative;font-family:"Arimo",Arial,sans-serif;color:var(--ink)}
a{color:inherit;text-decoration:none}

/* header */
.site-header{position:absolute;left:14px;top:8px;width:1174px;height:160px;background:var(--sage)}
.site-header__frame{position:absolute;left:12px;top:9px;width:1150px;height:141px;border:1px solid var(--sage-line)}
.brand{position:absolute;left:34px;top:62px;font-family:"Arimo",Arial,sans-serif;font-weight:400;font-size:26px;line-height:1;color:var(--white);letter-spacing:1px}
.utility{position:absolute;right:24px;top:20px;display:flex;align-items:center;gap:14px;font-size:13px;color:var(--white)}
.utility__checkout{background:var(--charcoal);color:var(--white);border:1px solid #ddd;padding:5px 6px;margin-left:10px}
.search{position:absolute;right:24px;top:110px;display:flex;gap:7px}
.search__field{width:231px;height:26px;background:var(--white);border:1px solid #999;font-size:12px;padding:5px 8px;color:#222}
.search__button{width:88px;height:26px;background:var(--charcoal);color:var(--white);font-size:13px;display:flex;align-items:center;justify-content:center;border:1px solid #ccc}

/* nav */
.main-nav{position:absolute;left:14px;top:173px;width:1174px;height:51px;display:grid;grid-template-columns:98px 87px 142px 157px 67px 90px 148px 104px 88px 112px 81px;background:var(--ink)}
.main-nav__item{display:flex;align-items:center;justify-content:center;text-align:center;color:var(--white);font-size:16px;line-height:1;border-left:2px solid var(--white)}
.main-nav__item:first-child{border-left:none}
.main-nav__item--holiday{background:var(--violet)}

/* hero */
.hero{position:absolute;left:14px;top:237px;width:740px;height:588px;background:#000;overflow:hidden}
.hero__photo{position:absolute;left:0;top:70px;width:740px;height:518px;background:linear-gradient(160deg,#0b0b0b 0%,#1c1c1c 40%,#3a4a63 65%,#22262e 100%)}
.hero__number{position:absolute;left:44px;top:6px;font-family:"Bowlby One SC",sans-serif;font-size:126px;line-height:1;color:var(--crimson)}
.hero__percent{position:absolute;left:250px;top:28px;font-family:"Play",sans-serif;font-size:50px;line-height:1;color:var(--crimson)}
.hero__off{position:absolute;left:248px;top:66px;font-family:"Play",sans-serif;font-size:72px;line-height:1;color:var(--crimson)}
.hero__cta{position:absolute;left:389px;top:83px;width:190px;height:60px;background:var(--violet-btn);border:1px solid #d9b4f5;color:var(--white);font-family:"Play",sans-serif;font-size:29px;display:flex;align-items:center;justify-content:center}
.hero__line{position:absolute;left:44px;top:150px;font-family:"Michroma",sans-serif;font-size:30px;letter-spacing:8px;color:var(--white);-webkit-text-stroke:1.2px var(--white)}

/* promo tiles */
.promo{position:absolute;left:766px;width:422px;height:189px}
.promo--shirts{top:237px}.promo--gifts{top:436px}.promo--jewelry{top:635px}
.promo__card{position:absolute;left:0;top:0;width:141px;height:189px;background:linear-gradient(180deg,var(--tile-top),var(--tile-bottom));color:var(--white);padding:12px 0 0 16px;box-shadow:0 3px 5px rgba(0,0,0,.35);overflow:hidden}
.promo__script{font-family:"Great Vibes",cursive;font-size:46px;line-height:.9}
.promo__from{font-size:16px}
.promo__inline{display:flex;align-items:flex-end;gap:4px}
.promo__inline .promo__from{padding-bottom:4px}
.promo__brand{font-family:"Oswald",sans-serif;font-weight:600;font-size:26px;line-height:1.05;text-transform:uppercase;margin-top:4px}
.promo__link{position:absolute;left:16px;bottom:22px;font-size:14px}
.promo__photo{position:absolute;left:145px;top:0;width:277px;height:189px}
.promo--shirts .promo__photo{background:linear-gradient(90deg,#e9e070,#5aa8c8 25%,#3b58b5 50%,#6f55c4 65%,#e8e8ee 85%,#f4f4f6)}
.promo--gifts .promo__photo{background:radial-gradient(circle at 55% 50%,#c98a2a 0%,#7a1a12 35%,#2a0606 80%)}
.promo--jewelry .promo__photo{background:radial-gradient(circle at 40% 60%,#8a5a22 0%,#3a2a14 45%,#0c0a06 85%)}

/* footer */
.site-footer{position:absolute;left:14px;top:840px;width:1174px;height:239px;background:var(--sage)}
.footer-col{position:absolute;top:24px}
.footer-col h3{font-weight:400;font-size:14px;margin-bottom:10px}
.footer-col li{list-style:none;font-size:11px;line-height:26px}
.signup{position:absolute;left:823px;top:14px;width:338px;height:145px;border:1px solid var(--sage-line);padding:12px 16px}
.signup h3{font-weight:400;font-size:14px;margin-bottom:14px}
.signup p{font-size:11px;line-height:20px;margin-bottom:10px}
.signup__row{display:flex;gap:8px}
.signup__field{width:216px;height:30px;background:var(--white);border:1px solid #777}
.signup__button{width:82px;height:30px;background:var(--charcoal);color:var(--white);font-size:14px;display:flex;align-items:center;justify-content:center;border:1px solid #ccc}
.legal{position:absolute;left:0;right:0;top:184px;text-align:center;font-size:11px;line-height:16px}
</style>
</head>
<body>

<header class="site-header">
  <div class="site-header__frame"></div>
  <a class="brand" href="#">Orlin House</a>
  <nav class="utility">
    <a href="#">ABOUT VELMORA</a>
    <a href="#">CUSTOMER SERVICE</a>
    <a href="#">MY ACCOUNT (SIGN IN)</a>
    <a href="#">SHOPPING BAG &nbsp;( 0 ITEMS)</a>
    <a class="utility__checkout" href="#">CHECK OUT</a>
  </nav>
  <form class="search">
    <div class="search__field">Keyword or item#</div>
    <div class="search__button">SEARCH</div>
  </form>
</header>

<nav class="main-nav">
  <a class="main-nav__item" href="#">WHAT'S<br>NEW</a>
  <a class="main-nav__item" href="#">DECOR</a>
  <a class="main-nav__item" href="#">FURNISHINGS</a>
  <a class="main-nav__item" href="#">DINNING &amp;<br>ENTERTAINING</a>
  <a class="main-nav__item" href="#">BED &amp;<br>BATH</a>
  <a class="main-nav__item" href="#">OFFICE</a>
  <a class="main-nav__item" href="#">APPAREL &amp;<br>ACCESSORIES</a>
  <a class="main-nav__item" href="#">JEWELRY</a>
  <a class="main-nav__item" href="#">GIFTS</a>
  <a class="main-nav__item main-nav__item--holiday" href="#">HOLIDAY<br>SHOP</a>
  <a class="main-nav__item" href="#">SALE</a>
</nav>

<section class="hero">
  <div class="hero__photo" role="img" aria-label="Photo of a male model reclining in a denim jacket and jeans"></div>
  <div class="hero__number">20</div>
  <div class="hero__percent">%</div>
  <div class="hero__off">OFF</div>
  <a class="hero__cta" href="#">SHOP NOW</a>
  <div class="hero__line">ON MENS APPAREL</div>
</section>

<a class="promo promo--shirts" href="#">
  <div class="promo__card">
    <div class="promo__script">Shirts</div>
    <div class="promo__from" style="padding-left:18px">FROM</div>
    <div class="promo__brand">Harlow<br>Pierce</div>
    <div class="promo__link">SHOP NOW »</div>
  </div>
  <div class="promo__photo" role="img" aria-label="Photo of colourful shirts hanging on a rail"></div>
</a>

<a class="promo promo--gifts" href="#">
  <div class="promo__card">
    <div class="promo__inline"><span class="promo__script">Gifts</span><span class="promo__from">FROM</span></div>
    <div class="promo__brand" style="font-size:24px">Bramwell</div>
    <div class="promo__link">SHOP NOW »</div>
  </div>
  <div class="promo__photo" role="img" aria-label="Illustration of a golden gift bow with snowflakes on deep red"></div>
</a>

<a class="promo promo--jewelry" href="#">
  <div class="promo__card">
    <div class="promo__from" style="padding-left:48px;margin-top:6px">FREE</div>
    <div class="promo__script" style="font-size:36px">Shipping</div>
    <div class="promo__from" style="margin-top:18px">FOR &nbsp;JEWELRY</div>
    <div class="promo__link">SHOP NOW »</div>
  </div>
  <div class="promo__photo" role="img" aria-label="Photo of beaded necklaces and amber jewellery"></div>
</a>

<footer class="site-footer">
  <div class="footer-col" style="left:21px">
    <h3>CUSTOMER SERVICE</h3>
    <ul><li>LIVE CHAT</li><li>CUSTOMER SERVICE</li><li>CONTACT ORLINHOUSE</li><li>CONCIERGE</li></ul>
  </div>
  <div class="footer-col" style="left:232px">
    <h3>OUR GURANTEE</h3>
    <ul><li>SHIPPING INFORMATION</li><li>ORDERING AND PAYMENT</li><li>RETURNS AND EXCHANGES</li><li>PRIVACY AND SECURITY</li></ul>
  </div>
  <div class="footer-col" style="left:443px">
    <h3>ONLINE SHOPPING</h3>
    <ul><li>BUSINESS GIFTS</li><li>GIFT REGISTRY</li><li>WISH LIST</li><li>AFFILIATES</li></ul>
  </div>
  <div class="footer-col" style="left:654px">
    <h3>OUR COMMUNITY</h3>
    <ul><li>STORE EVENTS</li><li>DESIGN TRADE</li><li>CATALOGUE REQUESTS</li><li>FOLLOW US</li></ul>
  </div>
  <form class="signup">
    <h3>SIGN UP FOR EMAIL</h3>
    <p>JOIN OUR E-MAIL LIST TO LEARN ABOUT NEW PRODUCTS, SPECIAL OFFERS AND STORE EVENTS.</p>
    <div class="signup__row"><div class="signup__field"></div><div class="signup__button">SUBMIT</div></div>
  </form>
  <div class="legal">FOR QUESTION OR ASSISTANCE CALL US AT 1.800.555.0142<br>© 2012 ORLIN HOUSE</div>
</footer>

</body>
</html>
```